Home page web design for "Tales from Thee"

We need a home page web design for a start up company that will write memoirs for seniors.
The completed project will need to include PSD files...NO HTML or CSS necessary.
Attached is a brief outline concept that may give you some ideas...but you are the creative professionals, so please feel free to add your ideas. We will also attach some files that show you our logo, brochures, and photos that could be used to give you ideas of our focus.
There will need to be access to the other pages on the home page to include: 'About Us'; 'How We Can Help'; 'Community Sessions'; 'Senior Consulting ' and 'Contact Us'.
Updates

Target Market(s)

Seniors and Baby Boomers

Industry/Entity Type

It Company

Number of Pages Required

1 page

Colors
f9ba93
fbca95
faa54b
faf289
f37123

Requirements
Must have
• Script easy on senior eyes.
• Initial contact number would be 844-4LANTERN
Nice to have
• While the color pallet is non-specific we prefer the warm colors.
• salmon, peach.......
• NOT so much the orange of Halloween:)
• However, please utilize your creativity and put in colors you feel will draw best with your design.

```html
<!DOCTYPE html>
<html lang="en">
<head>
<meta charset="utf-8">
<title>Tales from Thee — Home</title>
<link rel="stylesheet" href="https://fonts.googleapis.com/css2?family=Tinos:ital,wght@0,400;0,700;1,400;1,700&display=swap">
<style>
  :root {
    --page: #fbca95;
    --cream: #fdf1e2;
    --frame: #fef4e8;
    --panel-line: #f2b98a;
    --orange: #f37123;
    --orange-soft: #faa54b;
    --text: #4a3426;
    --muted: #8a6b55;
    --rule: #c9956a;
    --nav-active: #c79a73;
  }
  * { margin: 0; padding: 0; box-sizing: border-box; }
  html, body { width: 1200px; height: 1148px; overflow: hidden; }
  body {
    background: var(--page);
    font-family: "Tinos", "Times New Roman", serif;
    color: var(--text);
    position: relative;
  }
  .brand {
    position: absolute; left: 472px; top: 28px; width: 256px; height: 124px;
    display: flex; align-items: center; justify-content: center;
  }
  .brand-name {
    font-size: 30px; color: var(--orange); font-weight: 400;
    letter-spacing: 0.5px;
  }
  .tagline {
    position: absolute; left: 89px; top: 160px; width: 1027px; height: 20px;
    display: flex; align-items: center; gap: 18px;
  }
  .tagline::before, .tagline::after {
    content: ""; flex: 1; height: 1px; background: var(--rule);
  }
  .tagline span { font-style: italic; font-size: 16px; color: var(--muted); }
  .main-nav {
    position: absolute; left: 89px; top: 190px; width: 1027px; height: 33px;
    background: #fff; display: flex; align-items: stretch;
  }
  .main-nav a {
    text-decoration: none; color: var(--text); font-size: 15px;
    display: flex; align-items: center; justify-content: center;
  }
  .nav-home { width: 89px; background: var(--nav-active); color: #fff !important; }
  .nav-item { flex: 1; }
  .nav-call {
    width: 188px; background: var(--orange-soft); color: #fff !important;
    font-weight: 700; letter-spacing: 1px; gap: 10px; font-size: 14px !important;
  }
  .photo-frame {
    position: absolute; background: var(--frame); padding: 8px;
    box-shadow: 0 0 0 1px rgba(201,149,106,0.25);
  }
  .photo { width: 100%; height: 100%; }
  .photo-writing { left: 89px; top: 249px; width: 274px; height: 423px; }
  .photo-writing .photo { background: linear-gradient(135deg, #7a3f22, #c58a5a 60%, #e8d2c0); }
  .photo-hands { left: 89px; top: 692px; width: 274px; height: 305px; }
  .photo-hands .photo { background: linear-gradient(160deg, #f1e6e0, #c9a596 55%, #efe4dd); }
  .photo-reader { left: 840px; top: 247px; width: 276px; height: 403px; }
  .photo-reader .photo { background: linear-gradient(150deg, #6a5a48, #c7a88e 45%, #2f3440); }
  .photo-shore { left: 840px; top: 669px; width: 276px; height: 328px; }
  .photo-shore .photo { background: linear-gradient(180deg, #5e6a8a, #c88d84 55%, #2b2326); }
  .story-panel {
    position: absolute; left: 377px; top: 246px; width: 448px; height: 751px;
    background: var(--frame); padding: 6px;
  }
  .story-inner {
    border: 1px solid var(--panel-line); height: 100%; padding: 20px 28px 0 28px;
  }
  .story-title {
    text-align: center; color: var(--orange); font-style: italic; font-weight: 700;
    font-size: 30px; line-height: 31px; margin-bottom: 18px;
  }
  .story-inner p {
    font-size: 15.3px; line-height: 19.8px; text-align: justify; margin-bottom: 20px;
  }
  .story-links {
    display: flex; justify-content: space-between; align-items: flex-start; margin-top: -8px;
  }
  .story-links a { color: var(--text); font-size: 13px; line-height: 14px; }
  .gift-link { display: block; width: 34px; }
  .more-link { display: flex; align-items: center; gap: 6px; }
  .footer-rule {
    position: absolute; left: 94px; width: 1012px; border-top: 1px dashed #e2ad7f;
  }
  .contact-block {
    position: absolute; left: 484px; top: 1042px; width: 236px; height: 42px;
    border-left: 1px dashed var(--rule); border-right: 1px dashed var(--rule);
    display: flex; flex-direction: column; align-items: center; justify-content: space-between;
    font-size: 14.5px; color: var(--muted); letter-spacing: 1px;
  }
  .contact-line { display: flex; align-items: center; gap: 12px; }
  .copyright {
    position: absolute; left: 0; top: 1119px; width: 1200px; text-align: center;
    font-size: 11.5px; color: var(--orange-soft);
  }
</style>
</head>
<body>
  <header>
    <div class="brand"><span class="brand-name">Tales from Thee</span></div>
    <div class="tagline"><span>Ordinary Lives……… Extraordinary Legacies</span></div>
    <nav class="main-nav">
      <a class="nav-home" href="#">Home</a>
      <a class="nav-item" href="#">About Us</a>
      <a class="nav-item" href="#">How We Can Help</a>
      <a class="nav-item" href="#">Community Services</a>
      <a class="nav-item" href="#">Senior Consulting Services</a>
      <a class="nav-item" href="#">Contact Us</a>
      <a class="nav-call" href="#">
        <svg width="20" height="20" viewBox="0 0 20 20" aria-hidden="true"><circle cx="10" cy="10" r="9" fill="none" stroke="#fff" stroke-width="1.6"/><path d="M7 5.5l1.8 2.3-1 1.2c.6 1.2 1.6 2.2 2.8 2.8l1.2-1 2.3 1.8-.9 1.6c-3.6-.4-6.6-3.4-7-7z" fill="#fff"/></svg>
        844-4LANTERN
      </a>
    </nav>
  </header>

  <main>
    <figure class="photo-frame photo-writing"><div class="photo" role="img" aria-label="Photo of an elderly woman writing letters at a wooden desk by lamplight"></div></figure>
    <figure class="photo-frame photo-hands"><div class="photo" role="img" aria-label="Close-up photo of two elderly hands clasped together on white linen"></div></figure>

    <article class="story-panel">
      <div class="story-inner">
        <h1 class="story-title">When a genealogy<br>doesn’t say enough!</h1>
        <p>If you were alive in 100 years, what would you share with your descendants?</p>
        <p>Now you have a vehicle to help you immortalize your thoughts for the future…specifically for those who will want to know!</p>
        <p>We are not all presidents of countries or CEO’s of fortune 500 companies! But “every life legacy is a gift to be treasured by the next generation.”</p>
        <p>Does your family host generations of soldiers, doctors, farmers, scientists, mechanics, entrepreneurs, writers, politicians, contractors, pastors, artisans, athletes, musicians, etc..? Generational patterns can often emerge when writing your story that will interest the next generation.</p>
        <p>A genealogy, while very relevant, doesn’t offer the personal story of the names we find. A biography can place a deeper relevance on the face for future descendants. Every life is a legacy to pass forward and we at Tales from Thee believe everyone should chronicle their life journey in writing. This commitment allows you to be remembered for who you truly are as a person.</p>
        <p>Think about it….Do you know the triumphs and tribulations of your ancestors? Do you wish you did? Well, so will those falling into your personal family tree.</p>
        <div class="story-links">
          <a class="gift-link" href="#">Great Gift Idea</a>
          <a class="more-link" href="#">
            <svg width="11" height="11" viewBox="0 0 11 11" aria-hidden="true"><circle cx="5.5" cy="5.5" r="5.5" fill="#f37123"/><path d="M4.3 3l2.6 2.5-2.6 2.5" fill="none" stroke="#fff" stroke-width="1.4"/></svg>
            Learn More
          </a>
        </div>
      </div>
    </article>

    <figure class="photo-frame photo-reader"><div class="photo" role="img" aria-label="Photo of an elderly man holding up his printed memoir book"></div></figure>
    <figure class="photo-frame photo-shore"><div class="photo" role="img" aria-label="Photo of an elderly couple walking along a beach at sunset"></div></figure>
  </main>

  <footer>
    <div class="footer-rule" style="top:1021px"></div>
    <div class="contact-block">
      <span class="contact-line">
        <svg width="13" height="13" viewBox="0 0 13 13" aria-hidden="true"><path d="M2 1l3 3-1.5 1.6c.9 1.7 2.2 3 3.9 3.9L9 8l3 3-1.6 1.6C5.8 12.2.8 7.2.4 2.6z" fill="#8a6b55"/></svg>
        555-210-4817
      </span>
      <span class="contact-line">
        <svg width="13" height="10" viewBox="0 0 13 10" aria-hidden="true"><rect x=".6" y=".6" width="11.8" height="8.8" fill="none" stroke="#8a6b55" stroke-width="1.2"/><path d="M.6.6l5.9 4.6 5.9-4.6" fill="none" stroke="#8a6b55" stroke-width="1.2"/></svg>
        info@talesfromthee.com
      </span>
    </div>
    <div class="footer-rule" style="top:1104px"></div>
    <p class="copyright">Copyright © Talesfromthee.com</p>
  </footer>
</body>
</html>
```